KLMR stationery 2023

Our stationery dates back to 2007 when we changed practice rooms.
We would like to have kept the logo and spiced up the design, especially since we have one more colleague (Dr. Henriette Bollmeyer)
Our practice colors are a slightly more muted pink and sand-colored.
Follow-up orders for flyers, notices, etc. are still waiting for this design.

```html
<!DOCTYPE html>
<html lang="de">
<head>
<meta charset="utf-8">
<title>KLMR Briefpapier</title>
<link href="https://fonts.googleapis.com/css2?family=Arimo:wght@400;700&family=Source+Sans+3:wght@400&display=swap" rel="stylesheet">
<style>
  :root {
    --backdrop: #dedede;
    --paper: #ffffff;
    --accent: #ee3fe0;
    --ink-dark: #1e1e1e;
    --ink-mid: #555555;
    --ink-body: #8a8a8a;
    --rule: #9a9a9a;
    --art-light: #f7f7f7;
    --art-mid: #ededed;
  }
  html, body {
    margin: 0; padding: 0;
    width: 1200px; height: 1200px;
    overflow: hidden;
    background: var(--backdrop);
  }
  .letterhead {
    position: absolute;
    left: 242px; top: 93px;
    width: 716px; height: 1014px;
    background: var(--paper);
    font-family: "Arimo", Arial, sans-serif;
  }
  .brand {
    position: absolute; left: 38px; top: 52px;
    display: flex; align-items: center; gap: 10px;
  }
  .brand-dot {
    width: 38px; height: 38px; border-radius: 50%;
    background: var(--accent);
  }
  .brand-name {
    font-family: "Arimo", Arial, sans-serif;
    font-size: 50px; line-height: 1; letter-spacing: 4px;
    color: var(--ink-dark); font-weight: 400;
  }
  .divider {
    position: absolute; top: 42px; width: 2px; height: 65px;
    background: var(--accent);
  }
  .divider--first { left: 293px; }
  .divider--second { left: 481px; }
  .doctors {
    position: absolute; left: 314px; top: 44px;
    margin: 0; padding: 0; list-style: none;
    font-size: 12px; line-height: 14.5px; color: var(--ink-mid);
  }
  .contacts {
    position: absolute; left: 504px; top: 44px;
    margin: 0; padding: 0; list-style: none;
    font-family: "Source Sans 3", Arial, sans-serif;
    font-size: 12px; line-height: 14.5px; color: var(--ink-mid);
  }
  .contacts li { display: flex; align-items: center; gap: 5px; }
  .contacts svg { width: 9px; height: 9px; fill: var(--accent); flex: none; }
  .contacts .address { margin-top: 1px; }
  .salutation {
    position: absolute; left: 66px; top: 314px; margin: 0;
    font-family: "Source Sans 3", Arial, sans-serif;
    font-size: 15px; font-weight: 400; color: var(--ink-body);
  }
  .letter-body {
    position: absolute; left: 64px; top: 360px; width: 590px;
    font-size: 11.9px; line-height: 14.6px; color: var(--ink-body);
  }
  .letter-body p { margin: 0 0 13px; }
  .closing {
    position: absolute; left: 66px; top: 663px; margin: 0;
    font-family: "Source Sans 3", Arial, sans-serif;
    font-size: 9px; color: var(--ink-body);
  }
  .practice-art {
    position: absolute; left: 134px; top: 675px;
    width: 578px; height: 240px;
    background: radial-gradient(ellipse at 45% 55%, var(--art-mid), var(--art-light) 60%, var(--paper) 100%);
  }
  .hours {
    position: absolute; left: 0; right: 0; top: 930px; margin: 0;
    text-align: center; font-size: 14px; font-weight: 700; color: var(--accent);
  }
  .footer-rule {
    position: absolute; left: 56px; width: 604px; top: 954px;
    height: 1px; background: var(--rule);
  }
  .services {
    position: absolute; left: 0; right: 0; top: 959px;
    text-align: center; font-size: 11.8px; line-height: 15px; color: var(--ink-mid);
  }
  .services p { margin: 0; }
  .services .bullet { color: var(--accent); font-size: 9px; vertical-align: 1px; padding: 0 3px; }
  .accent-band {
    position: absolute; left: 0; right: 0; bottom: 0; height: 13px;
    background: var(--accent);
  }
</style>
</head>
<body>
<main class="letterhead">
  <header>
    <div class="brand">
      <span class="brand-dot"></span>
      <span class="brand-name">KLMR</span>
    </div>
    <span class="divider divider--first"></span>
    <ul class="doctors">
      <li>Dr. Marlene Oswald</li>
      <li>Dr. Petra Lindqvist</li>
      <li>Dr. Jonas Oswald</li>
      <li>Dr. Ilona Varga</li>
      <li>Dr. Henriette Bollmeyer</li>
    </ul>
    <span class="divider divider--second"></span>
    <ul class="contacts">
      <li><svg viewBox="0 0 10 10"><path d="M2 0.5l2 2-1 1.2c.6 1.3 1.5 2.2 2.8 2.8L7 5.5l2 2-1.2 1.6C4.5 9 1 5.5.9 2.2z"/></svg>041/555 12 40</li>
      <li><svg viewBox="0 0 10 10"><rect x="2.5" y="0.5" width="5" height="3"/><rect x="0.5" y="3.5" width="9" height="4.5" rx="1"/><rect x="2.5" y="7" width="5" height="2.5"/></svg>041/555 12 41</li>
      <li><svg viewBox="0 0 10 10"><path d="M0.5 2h9v6h-9z M0.5 2l4.5 3.5L9.5 2" /></svg>praxis.klmr@medmail.ch</li>
      <li><svg viewBox="0 0 10 10"><circle cx="5" cy="5" r="4.5"/></svg>www.klmr-praxis.ch</li>
      <li class="address">Birkenweg 14, 6300 Seedorf</li>
    </ul>
  </header>

  <h2 class="salutation">Dear Mr. Keller,</h2>

  <section class="letter-body">
    <p>Lorem ipsum dolor sit amet, consectetuer adipiscing elit, sed diam nonmmy nibh euismod tincidunt ut laor eet dolore magna aliquam erat volutpat. Ut wisi enim ad minim veniam, quis nostrud exerci tationmcorper suscipit lobortis nisl ut aliquip ex ea commodo consequat. Duis autem vel eum iriure dolor in hendrerit in vulputate velit esse molestie consequat, vel illum dolore eu feugiat</p>
    <p>Rorem ipsum dolor sit amet, consectetuer adipiscing elit, sed diam nonmmy nibh euismod tincidunt ut laor eet dolore magna aliquam erat volutpat. Ut wisi enim ad minim veniam, quis nostrud exerci tationmcorper suscipit lobortis nisl ut aliquip ex ea commodo consequat. Duis autem vel eum iriure dolor in hendrerit in vulputate velit esse molest</p>
    <p>Dorem ipsum dolor sit amet, consectetuer adipiscing elit, sed diam nonmmy nibh euismod tincidunt ut laor eet dolore magna aliquam erat volutpat. Ut wisi enim ad minim veniam, quis nostrud exerci tationmcorper suscipit lobortis nisl ut aliquip ex ea commodo consequat. Duis autem vel eum iriure dolor in hendrerit in suscipit lobortis nisl ut aliquip ex ea commodo consequat. Duis autem vel eum iriure dolor in hendrerit in vulputate velit esse molestie consequat, vel illum</p>
    <p>Sorem ipsum dolor sit amet, consectetuer adipiscing elit, sed diam nonmmy nibh euismod tincidunt ut laor eet dolore magna aliquam erat volutpat. Ut wisi enim ad minim veniam, quis nostrud exerci tationmcorper suscipit lobortis nisl ut aliquip ex ea commodo consequat. Duis autem vel eum iriure dolor in</p>
  </section>

  <p class="closing">Sincerely,</p>

  <div class="practice-art" role="img" aria-label="Faint pencil sketch of three women walking beside the practice building"></div>

  <footer>
    <p class="hours">Öffnungszeiten NEU: Montag - Freitag 08.00 - 12.00 Uhr und 13.00 - 17.00 Uhr</p>
    <span class="footer-rule"></span>
    <div class="services">
      <p><span class="bullet">●</span>Fachärzte für Gynäkologie und Geburtshilfe <span class="bullet">●</span>Pränataldiagnostik</p>
      <p><span class="bullet">●</span>Schwangerschaftsbetreuung <span class="bullet">●</span>Kinderwunschbehandlung <span class="bullet">●</span>Ambulante Operationen <span class="bullet">●</span>Onkologische Betreuung</p>
    </div>
    <span class="accent-band"></span>
  </footer>
</main>
</body>
</html>
```